Newsletter Ad

I am looking for someone to design an advertisement for a mother's club newsletter. 4" wide X by 5" tall (and 2.5" wide X 5" tall if possible).

I'm a psychotherapist, so want the ad to look professional, but modern. I have a logo with my photo attached that can be incorporated into the design. The colors of my website are turquoise and white. I'd like to keep with that theme...so maybe some turquoise blocking to match the logo font color.

I'm uploading a logo as well as an ad draft with the content I'd like listed in the ad.

```html
<!DOCTYPE html>
<html lang="en">
<head>
<meta charset="utf-8">
<title>Dana Reyes – Newsletter Ad</title>
<link rel="stylesheet" href="https://fonts.googleapis.com/css2?family=Jost:wght@400;500&family=Roboto+Condensed:wght@400;700&display=swap">
<style>
  :root {
    --teal: #4fa3a2;
    --white: #ffffff;
    --ink: #333333;
    --ink-soft: #444444;
    --photo-dark: #0b0908;
    --photo-warm: #9c7a5c;
    --photo-skin: #e7c3ad;
    --petal: #f1f3ea;
    --leaf: #c9d9b4;
    --flourish: #d9d4cf;
  }
  * { margin: 0; padding: 0; box-sizing: border-box; }
  html, body { width: 960px; height: 1200px; overflow: hidden; }
  body { background: var(--teal); position: relative; font-family: "Roboto Condensed", "Arial Narrow", sans-serif; }

  .ad { position: absolute; inset: 0; }

  .portrait {
    position: absolute; left: 36px; top: 36px; width: 888px; height: 656px;
    background:
      radial-gradient(ellipse 32% 42% at 58% 52%, var(--photo-skin) 0%, rgba(231,195,173,0.6) 55%, rgba(231,195,173,0) 100%),
      radial-gradient(ellipse 52% 70% at 56% 55%, var(--photo-warm) 0%, rgba(156,122,92,0.5) 60%, rgba(156,122,92,0) 100%),
      var(--photo-dark);
  }

  .name-block {
    position: absolute; left: 52px; top: 58px; width: 206px;
    color: var(--white); font-family: "Jost", "Futura", sans-serif;
  }
  .name-block .name { font-size: 40px; font-weight: 400; letter-spacing: 0.5px; line-height: 1; }
  .name-block .credentials { font-size: 22px; font-weight: 400; text-align: right; margin-top: 4px; letter-spacing: 0.5px; }

  .headline-band {
    position: absolute; left: 36px; top: 692px; width: 888px; height: 64px;
    display: flex; align-items: center; justify-content: center;
    color: var(--white); font-weight: 700; font-size: 36px; letter-spacing: 0.2px;
  }

  .info-panel { position: absolute; left: 36px; top: 756px; width: 888px; height: 407px; background: var(--white); }

  .lotus {
    position: absolute; left: 0; top: 24px; width: 134px; height: 383px;
    background: linear-gradient(180deg, var(--petal) 0%, #e9ecd9 45%, var(--petal) 70%, var(--leaf) 100%);
    border-radius: 0 60px 0 0;
  }

  .services { position: absolute; left: 0; top: 10px; width: 888px; text-align: center; color: var(--ink); font-size: 30px; line-height: 43px; }
  .services li { display: inline; list-style: none; margin: 0 10px; }
  .services li::before { content: "◆"; font-size: 18px; margin-right: 14px; vertical-align: 4px; }

  .flourish { position: absolute; left: 358px; width: 172px; height: 24px; background: var(--flourish); border-radius: 12px; }
  .flourish.top { top: 162px; }
  .flourish.bottom { top: 346px; }

  .contact { position: absolute; left: 0; top: 202px; width: 888px; text-align: center; color: var(--ink); font-size: 28px; line-height: 35px; }
  .contact .phone { font-weight: 700; font-size: 30px; color: var(--ink); }

  .license { position: absolute; right: 18px; bottom: 12px; font-size: 20px; color: var(--ink-soft); }
</style>
</head>
<body>
<main class="ad">
  <div class="portrait" role="img" aria-label="Smiling headshot portrait of the therapist against a black background"></div>

  <div class="name-block">
    <div class="name">DANA REYES</div>
    <div class="credentials">MA, MFT</div>
  </div>

  <h1 class="headline-band">Psychotherapy for Individuals, Couples and Families</h1>

  <section class="info-panel">
    <div class="lotus" role="img" aria-label="White lotus flowers rising along the left edge"></div>

    <ul class="services">
      <li>Parenting</li><li>Depression</li><li>Anxiety</li><li>Life Transitions</li><br>
      <li>Divorce</li><li>Couples Issues</li><li>Women’s Issues</li><br>
      <li>Attachment and Neuroscience</li>
    </ul>

    <div class="flourish top" role="img" aria-label="Decorative scroll divider"></div>

    <address class="contact" style="font-style: normal;">
      418 Harbor Lane, Bayside, CA 94920<br>
      www.danareyestherapy.com<br>
      dana@danareyestherapy.com<br>
      <span class="phone">415 555 0182</span>
    </address>

    <div class="flourish bottom" role="img" aria-label="Decorative scroll divider"></div>

    <p class="license">License# MFC48210</p>
  </section>
</main>
</body>
</html>
```